Psychologist in Private Practice Needs a Website Update

Project Description:
Hello talented designers! My current website, www.jodelbrisk.com, needs a fresh, boho-modern makeover that highlights the warm, welcoming nature of my holistic therapy practice. I want a website that has a serene, boho- modern design, appealing to clients seeking individual therapy, couples therapy, and family counseling.

I’d also like to prepare for a future second site focused exclusively on couples and family therapy. Both sites should be interconnected, so I’m looking for design suggestions that seamlessly link them together while maintaining a cohesive brand look and feel.

Key Objectives:

Boho-Modern Aesthetic: Incorporate natural textures, neutral or earthy tones, and clean lines that capture a modern, inviting vibe.

Responsive Design: Ensure the website is user-friendly on desktop, tablet, and mobile devices.

Clear Service Offerings: Prominently feature my three distinct services: individual therapy, couples therapy, and family counseling.

Interlinked Future Site: Provide ideas on how to cross-link this site with a second site focused on couples and family therapy.

User Experience (UX): Make the site simple to navigate, with intuitive placement of content that speaks to potential clients’ needs.

SEO-Friendly: Implement best practices for structure, site speed, and keyword usage to boost online visibility.

What I Have Now:
Existing website: www.jodelbrisk.com
Basic content and a logo that can be refined or updated to match the boho-modern feel
Rough style guide with brand elements open to a fresh interpretation

Preferred Style/Tone:
Boho-modern with earthy tones, subtle textures, and clean typography
Warm, empathetic, and approachable to align with the nature of therapy services
Slightly artistic or organic elements that evoke calm and connection

Potential for an ongoing design relationship!
Updates

Need extra days to review

Target Market(s)

I have a high functioning, professional clientele who doctors, lawyers, and leaders in their field.

Industry/Entity Type

healthcare/mental health

Coding

Coded - Design and coding required

Font styles to use
Other font styles liked:
• cormorant garamond for headers and Source Sans Pro for supporting text

Colors

Designer to choose colors to be used in the design.

Requirements
Must have
• Open, Harmonious Layout I’d like the overall design to feel upscale, humanistic, open and harmonious, with minimal divisions of space. Rather than traditional section dividers, please consider using images, subtle shifts in color, typography, or spacing to define sections. Hero Image & Inspiration Ideally, the first (hero) image should evoke a sense of awe or inspiration. Focus on simplicity and elegance so the design feels spacious and inviting, allowing the content and imagery to really stand out. Natural Flow Wherever possible, let the design elements flow naturally into each other, creating a sense of unity and cohesion throughout the site.
Nice to have
• 1. Full-Width Hero Image: • The homepage should feature a full-width hero image that extends edge-to-edge across the screen for a modern and visually immersive effect. • This image should set the tone for the website, reflecting a calming, humanistic/natural, and upscale feel. It could include subtle overlays or gradients to enhance readability of text and navigation elements. Ideally, this image should have one or two people in nature. The image could be slightly transparent to allow the text "holistic therapy" and the tagline "an integrative approach to transformation" to be easily visible. Please help me find a breath-taking image that evokes a sense of beauty, inspiration, awe or hope. 2. Menu Tabs Positioned Over the Image: • The menu tabs (navigation bar) should be positioned directly on top of the hero image, either centered or aligned to the top right/left, depending on the design. • The navigation bar should have a slightly transparent or solid background (depending on the image and visibility needs) to ensure the text is easily readable without detracting from the image. 3. Typography and Text Placement: • The text overlay on the hero image should use the selected fonts: • Cormorant Garamond for headers (e.g., the tagline or welcome message). • Source Sans Pro for any supporting text. 5. Seamless Transitions: • Below the full-width image, transitions into the next sections (like “About,” “Services,” or client-focused content) should be smooth, using full-width separators that maintain the cohesive, open layout style. 6. Color Palette: • A neutral and calming color palette should be used (e.g., soft blues, grays, whites, or very muted earth tones) to create a soothing atmosphere for visitors. This design approach ensures the homepage looks clean, modern, and professional while maintaining the calming and upscale aesthetic that reflects the values of my psychology practice

```html
<!DOCTYPE html>
<html lang="en">
<head>
<meta charset="utf-8">
<title>Dr. Jodel Brisk — Holistic Therapy</title>
<link href="https://fonts.googleapis.com/css2?family=Poppins:wght@300;400;500;600;700&family=Cormorant+Garamond:wght@400;500&family=Libre+Baskerville:wght@700&display=swap" rel="stylesheet">
<style>
:root{
  --teal:#3b97a8;
  --orange:#f4a65a;
  --cream:#f6efe9;
  --mist:#dbe7ea;
  --ink:#151515;
  --grey:#7b7b7b;
  --card:#f3f3f3;
  --white:#ffffff;
  --ornament-a:#f7e4d8;
  --ornament-b:#f3d6c4;
}
*{margin:0;padding:0;box-sizing:border-box}
html,body{width:1200px;height:5133px;overflow:hidden;background:var(--white)}
body{font-family:"Poppins",sans-serif;color:var(--ink)}
.page{position:relative;width:1200px;height:5133px;overflow:hidden}
.abs{position:absolute}
.bg{position:absolute;left:0;width:1200px}
.photo{position:absolute;overflow:hidden}
.btn{position:absolute;display:flex;align-items:center;justify-content:center;border-radius:30px;background:var(--teal);color:var(--white);font-size:13px;letter-spacing:4px;font-weight:500;text-transform:uppercase;text-decoration:none}
.btn--orange{background:var(--orange);font-size:10px;letter-spacing:2.5px;height:34px;width:134px}
.h2{position:absolute;font-weight:700;font-size:37px;line-height:48px;text-transform:uppercase;letter-spacing:.3px;white-space:nowrap}
.body{position:absolute;font-size:13px;line-height:22px;color:var(--grey);font-weight:400}
.ornament{position:absolute;border-radius:10px;background:linear-gradient(135deg,var(--ornament-a),var(--ornament-b))}

/* nav */
.logo{position:absolute;display:flex;align-items:center;gap:10px}
.logo__dot{width:36px;height:36px;border-radius:50%;background:#f3dcc0}
.logo__name{font-size:19px;font-weight:500;color:var(--teal);line-height:20px}
.logo__role{font-size:13px;color:var(--orange);line-height:16px;font-weight:400}
.nav{position:absolute;top:55px;left:365px;font-size:14px;font-weight:500}
.nav a{position:absolute;white-space:nowrap;color:var(--ink);text-decoration:none}

/* list */
.checks{position:absolute;list-style:none}
.checks li{display:flex;align-items:center;height:40px;font-size:14.5px;color:#333;white-space:nowrap}
.checks li svg{margin-right:18px;flex:none}

/* services */
.card{position:absolute;top:2536px;width:252px;height:300px;background:var(--card);border-radius:14px;text-align:center}
.card--active{border:2px solid #e2e2e2;background:#f6f6f6}
.card__icon{width:74px;height:74px;border-radius:50%;background:#dbeef1;margin:24px auto 0}
.card__title{color:var(--teal);font-size:16px;line-height:21px;margin-top:12px;font-weight:500}
.card__text{font-size:11.5px;line-height:20px;color:var(--grey);margin:18px 18px 0}
.card .btn{left:59px;top:284px}

/* testimonial */
.quote{position:absolute;left:258px;width:684px;top:3284px;text-align:center;font-family:"Cormorant Garamond",serif;font-size:25px;line-height:31px;letter-spacing:.6px;color:#6a6a6a}

/* blog */
.post{position:absolute;top:4065px;height:420px;background:var(--white);border-radius:14px;box-shadow:0 10px 30px rgba(0,0,0,.07)}
.post .photo{left:16px;top:16px;right:16px;height:240px}
.post__date{position:absolute;left:30px;top:232px;width:50px;height:50px;border-radius:50%;background:var(--teal);border:3px solid var(--white);color:var(--white);text-align:center;font-size:15px;font-weight:700;line-height:17px;padding-top:9px}
.post__date small{display:block;font-size:9px;font-weight:400;line-height:10px}
.post__cat{position:absolute;left:30px;top:325px;font-size:11px;color:var(--orange);letter-spacing:1px}
.post__title{position:absolute;left:30px;top:358px;width:230px;font-family:"Libre Baskerville",serif;font-size:15px;line-height:28px;font-weight:700}

/* footer */
.foot-h{position:absolute;top:4800px;color:var(--teal);font-weight:600;font-size:17px;letter-spacing:.5px;white-space:nowrap}
.foot-list{position:absolute;top:4850px;list-style:none;font-size:10px;color:#555}
.foot-list li{height:26px;display:flex;align-items:center;white-space:nowrap}
.foot-list li::before{content:"";width:9px;height:9px;border-radius:50%;background:var(--orange);margin-right:10px}
.contact{position:absolute;font-size:10px;color:#555;white-space:nowrap}
.fine{position:absolute;top:5004px;font-size:10px;color:#555;white-space:nowrap}
</style>
</head>
<body>
<div class="page">

<svg class="bg" style="top:0" width="1200" height="720" viewBox="0 0 1200 720" aria-hidden="true">
  <path fill="#f6efe9" d="M0 0H1200V640C1150 660 1110 630 1060 652 1000 680 960 640 900 668 840 700 790 650 730 676 670 702 620 660 560 690 500 712 450 668 390 690 320 714 260 672 200 700 140 722 80 690 0 710Z"/>
</svg>

<header>
  <div class="logo" style="left:62px;top:40px">
    <span class="logo__dot"></span>
    <div><div class="logo__name">Dr. Jodel Brisk</div><div class="logo__role">Licensed Psychologist</div></div>
  </div>
  <nav class="nav">
    <a style="left:0">HOME</a><a style="left:103px">ABOUT</a><a style="left:207px">SERVICES</a><a style="left:321px">TESTIMONIALS</a><a style="left:473px">CONTACT</a>
  </nav>
  <a class="btn" style="left:978px;top:44px;width:150px;height:40px;font-size:12px">Contact</a>
</header>

<section class="hero">
  <div class="photo" role="img" aria-label="Woman sitting peacefully with eyes closed in warm sunlight" style="left:820px;top:90px;width:380px;height:560px;background:radial-gradient(ellipse at 60% 45%,#d9c3b0 0,#efe3d8 55%,#f6efe9 80%)"></div>
  <div class="ornament" role="img" aria-label="Feather ornament" style="left:345px;top:580px;width:120px;height:120px"></div>
  <div class="ornament" role="img" aria-label="Feather ornament" style="left:1055px;top:590px;width:145px;height:50px"></div>
  <h1 class="abs" style="left:58px;top:258px;font-size:44px;font-weight:700;letter-spacing:.5px;white-space:nowrap">HOLISTIC THERAPY</h1>
  <p class="body" style="left:58px;top:326px;width:430px">Lorem ipsum dolor sit amet, consectetur adipiscing elit, sed do eiusmod tempor incididunt ut labore et dolore magna aliqua. Ut enim ad minim veniam, quis nostrud exercitation ullamco laboris nisi ut aliquip ex ea commodo consequat.</p>
  <a class="btn" style="left:58px;top:444px;width:162px;height:42px">Contact</a>
</section>

<section class="about">
  <svg class="abs" style="left:94px;top:826px" width="390" height="390" viewBox="0 0 390 390" aria-hidden="true">
    <circle cx="191" cy="194" r="184" fill="none" stroke="#3b97a8" stroke-width="9"/>
  </svg>
  <div class="photo" role="img" aria-label="Warm interior with wooden French doors" style="left:114px;top:848px;width:360px;height:360px;border-radius:50%;background:linear-gradient(160deg,#b9835a,#8a5a3a 55%,#c79a72)"></div>
  <div class="photo" role="img" aria-label="Portrait of the psychologist" style="left:266px;top:998px;width:310px;height:310px;border-radius:50%;border:8px solid #fff;background:radial-gradient(circle at 50% 45%,#e6c3a5,#a8714b 70%,#6e4a33)"></div>
  <div class="ornament" role="img" aria-label="Feather ornament" style="left:585px;top:865px;width:70px;height:95px"></div>
  <h2 class="h2" style="left:665px;top:904px">ABOUT ME</h2>
  <p class="body" style="left:665px;top:974px;width:450px">Lorem ipsum dolor sit amet, consectetur adipiscing elit, sed do eiusmod tempor incididunt ut labore et dolore magna aliqua. Ut enim ad minim veniam, quis nostrud exercitation ullamco laboris nisi ut aliquip ex ea commodo consequat.</p>
  <p class="body" style="left:665px;top:1084px;width:450px">Duis aute irure dolor in reprehenderit in voluptate velit esse cillum dolore eu fugiat nulla pariatur. Excepteur sint occaecat cupidatat non proident, sunt in culpa qui officia deserunt mollit anim id est laborum.</p>
  <a class="btn" style="left:665px;top:1210px;width:168px;height:42px">Contact</a>
</section>

<svg class="bg" style="top:1420px" width="1200" height="860" viewBox="0 0 1200 860" aria-hidden="true">
  <path fill="#dbe7ea" d="M0 160C60 110 120 110 180 80 260 40 340 60 420 40 520 20 600 60 700 30 760 12 800 0 840 20 900 50 960 30 1040 60 1110 80 1160 60 1200 90V690C1150 700 1100 740 1030 720 960 700 900 760 820 740 740 720 680 780 600 770 520 760 470 800 400 790 330 780 280 830 240 800 200 770 150 700 60 700 30 700 10 690 0 690Z"/>
</svg>
<section class="partnership">
  <div class="ornament" role="img" aria-label="Feather ornament" style="left:58px;top:1595px;width:72px;height:95px"></div>
  <h2 class="h2" style="left:152px;top:1650px">THERAPY IS A<br>PARTNERSHIP.</h2>
  <p class="body" style="left:143px;top:1776px;width:440px">Lorem ipsum dolor sit amet, consectetur adipiscing elit, sed do eiusmod tempor incididunt ut labore et dolore magna aliqua. Ut enim ad minim veniam, quis nostrud exercitation ullamco laboris nisi ut aliquip ex ea commodo consequat.</p>
  <ul class="checks" style="left:143px;top:1882px">
    <li><svg width="28" height="28" viewBox="0 0 28 28"><circle cx="14" cy="14" r="12" fill="none" stroke="#f4a65a" stroke-width="1.6"/><path d="M9 14h10M15 10l4 4-4 4" fill="none" stroke="#f4a65a" stroke-width="1.6"/></svg>Feel overwhelmed with depression or anxiety.</li>
    <li><svg width="28" height="28" viewBox="0 0 28 28"><circle cx="14" cy="14" r="12" fill="none" stroke="#f4a65a" stroke-width="1.6"/><path d="M9 14h10M15 10l4 4-4 4" fill="none" stroke="#f4a65a" stroke-width="1.6"/></svg>Experience a lack of connection in your marriage.</li>
    <li><svg width="28" height="28" viewBox="0 0 28 28"><circle cx="14" cy="14" r="12" fill="none" stroke="#f4a65a" stroke-width="1.6"/><path d="M9 14h10M15 10l4 4-4 4" fill="none" stroke="#f4a65a" stroke-width="1.6"/></svg>Have a history of trauma or abuse</li>
    <li><svg width="28" height="28" viewBox="0 0 28 28"><circle cx="14" cy="14" r="12" fill="none" stroke="#f4a65a" stroke-width="1.6"/><path d="M9 14h10M15 10l4 4-4 4" fill="none" stroke="#f4a65a" stroke-width="1.6"/></svg>Worry excessively about what others think.</li>
    <li><svg width="28" height="28" viewBox="0 0 28 28"><circle cx="14" cy="14" r="12" fill="none" stroke="#f4a65a" stroke-width="1.6"/><path d="M9 14h10M15 10l4 4-4 4" fill="none" stroke="#f4a65a" stroke-width="1.6"/></svg>Struggle with other life challenges.</li>
  </ul>
  <div class="photo" role="img" aria-label="Woman meditating outdoors among autumn trees" style="left:668px;top:1648px;width:404px;height:404px;border-radius:50%;border:10px solid #fff;box-shadow:0 0 0 2px #333;background:radial-gradient(circle at 50% 40%,#c9a07a,#a8682c 55%,#5d4a2c)"></div>
</section>

<section class="services">
  <div class="ornament" role="img" aria-label="Feather ornament" style="left:380px;top:2390px;width:70px;height:90px"></div>
  <h2 class="h2" style="left:457px;top:2426px">OUR SERVICES</h2>
  <article class="card" style="left:52px"><div class="card__icon" role="img" aria-label="Individual therapy icon"></div><h3 class="card__title">Individual<br>Therapy</h3><p class="card__text">Lorem ipsum dolor sit amet, consectetur adipiscing elit, sed do eiusmod tempor incididunt ut labore et dolore magna aliqua.</p><a class="btn btn--orange">Read More</a></article>
  <article class="card" style="left:332px"><div class="card__icon" role="img" aria-label="Family therapy icon"></div><h3 class="card__title">Family<br>Therapy</h3><p class="card__text">Lorem ipsum dolor sit amet, consectetur adipiscing elit, sed do eiusmod tempor incididunt ut labore et dolore magna aliqua.</p><a class="btn btn--orange">Read More</a></article>
  <article class="card card--active" style="left:612px"><div class="card__icon" role="img" aria-label="Couple therapy icon"></div><h3 class="card__title">Couple<br>Therapy</h3><p class="card__text">Lorem ipsum dolor sit amet, consectetur adipiscing elit, sed do eiusmod tempor incididunt ut labore et dolore magna aliqua.</p><a class="btn btn--orange" style="left:57px;top:282px">Read More</a></article>
  <article class="card" style="left:892px"><div class="card__icon" role="img" aria-label="Mindfulness icon"></div><h3 class="card__title" style="margin-top:22px">Mindfullness</h3><p class="card__text" style="margin-top:28px">Lorem ipsum dolor sit amet, consectetur adipiscing elit, sed do eiusmod tempor incididunt ut labore et dolore magna aliqua.</p><a class="btn btn--orange">Read More</a></article>
</section>

<svg class="bg" style="top:2990px" width="1200" height="860" viewBox="0 0 1200 860" aria-hidden="true">
  <path fill="#f6efe9" d="M0 40C80 20 160 60 260 30 360 0 440 50 540 30 640 10 720 40 820 20 920 0 1000 40 1100 20 1150 12 1180 30 1200 26V800C1140 780 1100 820 1040 790 960 760 900 720 820 740 740 760 680 730 600 720 520 710 440 760 360 740 280 720 220 780 150 760 90 740 40 700 0 720Z"/>
</svg>
<section class="testimonials">
  <div class="ornament" role="img" aria-label="Feather ornament" style="left:380px;top:3115px;width:70px;height:90px"></div>
  <h2 class="h2" style="left:457px;top:3150px">TESTIMONIALS</h2>
  <blockquote class="quote">"Blandit massa enim nec dui. Eu facilisis sed odio morbi. Amet nisl purus in mollis nunc sed id. Ipsum dolor sit amet consectetur adipiscing elit. Orci eu lobortis elementum nibh tellus molestie nunc non blandit. Nulla posuere sollicitudin aliquam ultrices sagittis orci a scelerisque."</blockquote>
  <div class="photo" role="img" aria-label="Client portrait" style="left:526px;top:3458px;width:60px;height:60px;border-radius:50%;background:radial-gradient(circle,#c99a6a,#8a6236)"></div>
  <div class="abs" style="left:604px;top:3474px;font-size:12px;color:#999;white-space:nowrap">Maren Holt</div>
  <div class="abs" style="left:604px;top:3496px;font-size:9px;color:#aaa">Customer</div>
  <div class="abs" style="left:588px;top:3560px;display:flex;gap:10px"><span style="width:5px;height:5px;border-radius:50%;background:#f4c79a"></span><span style="width:5px;height:5px;border-radius:50%;background:var(--orange)"></span><span style="width:5px;height:5px;border-radius:50%;background:#f4c79a"></span></div>
</section>

<section class="blog">
  <div class="ornament" role="img" aria-label="Feather ornament" style="left:358px;top:3915px;width:72px;height:95px"></div>
  <h2 class="h2" style="left:435px;top:3950px">LATEST FROM BLOG</h2>
  <article class="post" style="left:86px;width:328px"><div class="photo" role="img" aria-label="Therapist comforting a patient in a bright office" style="background:linear-gradient(135deg,#e9e4dd,#d6c6b4 60%,#f0ece6)"></div><div class="post__date">03<small>Jan</small></div><span class="post__cat">— THERAPY</span><h3 class="post__title">Individual Treatment and Assistance</h3></article>
  <article class="post" style="left:444px;width:328px"><div class="photo" role="img" aria-label="Hands holding in a supportive gesture" style="background:linear-gradient(135deg,#cdb6a3,#9a7c66 60%,#d8c6b6)"></div><div class="post__date">03<small>Jan</small></div><span class="post__cat">— THERAPY</span><h3 class="post__title" style="width:180px">Communication in Relationships</h3></article>
  <article class="post" style="left:802px;width:330px"><div class="photo" role="img" aria-label="Counselling session between two adults" style="background:linear-gradient(135deg,#e8e6e2,#b9b2a8 60%,#dcd8d2)"></div><div class="post__date">03<small>Jan</small></div><span class="post__cat">— THERAPY</span><h3 class="post__title" style="width:270px">Finding a Great Therapist for Your Child</h3></article>
</section>

<svg class="bg" style="top:4620px" width="1200" height="513" viewBox="0 0 1200 513" aria-hidden="true">
  <path fill="#dbe7ea" d="M0 90C70 60 130 90 200 70 280 50 360 90 440 60 520 30 580 70 660 40 720 18 760 0 820 30 900 60 960 30 1040 50 1110 70 1160 40 1200 60V513H0Z"/>
</svg>
<footer>
  <div class="logo" style="left:125px;top:4836px">
    <span class="logo__dot"></span>
    <div><div class="logo__name">Dr. Jodel Brisk</div><div class="logo__role">Licensed Psychologist</div></div>
  </div>
  <h4 class="foot-h" style="left:398px">QUICK LINKS</h4>
  <ul class="foot-list" style="left:390px"><li>Home</li><li>About</li><li>Services</li><li>Blog</li><li>Contact</li></ul>
  <h4 class="foot-h" style="left:642px">SERVICES</h4>
  <ul class="foot-list" style="left:652px"><li>Individual Therapy</li><li>Family Therapy</li><li>Couple Therapy</li><li>Mindfulness</li><li>Relation Issue</li></ul>
  <h4 class="foot-h" style="left:846px">CONTACT INFO</h4>
  <svg class="abs" style="left:872px;top:4848px" width="14" height="14" viewBox="0 0 24 24"><path fill="#f4a65a" d="M6.6 10.8a15 15 0 006.6 6.6l2.2-2.2c.3-.3.7-.4 1-.2 1.1.4 2.3.6 3.6.6.6 0 1 .4 1 1V20c0 .6-.4 1-1 1A17 17 0 013 4c0-.6.4-1 1-1h3.5c.6 0 1 .4 1 1 0 1.3.2 2.5.6 3.6.1.3 0 .7-.2 1z"/></svg>
  <div class="contact" style="left:898px;top:4849px">(555) 014-2290</div>
  <svg class="abs" style="left:872px;top:4884px" width="16" height="14" viewBox="0 0 24 20"><rect x="1" y="2" width="22" height="16" rx="2" fill="#f4a65a"/><path d="M2 4l10 7 10-7" fill="none" stroke="#fff" stroke-width="1.6"/></svg>
  <div class="contact" style="left:898px;top:4885px">hello@jodelbrisk.com</div>
  <svg class="abs" style="left:874px;top:4918px" width="12" height="16" viewBox="0 0 24 32"><path fill="#f4a65a" d="M12 0C5.4 0 0 5.4 0 12c0 9 12 20 12 20s12-11 12-20C24 5.4 18.6 0 12 0zm0 17a5 5 0 110-10 5 5 0 010 10z"/></svg>
  <div class="contact" style="left:898px;top:4920px">18 Willow Lane, Larkspur</div>
  <p class="fine" style="left:130px">©2025 Jodel A. Brisk, Psy.D., All Rights Reserved.</p>
  <p class="fine" style="left:846px">Privacy Policy &nbsp;|&nbsp; Term and Conditions</p>
</footer>

</div>
</body>
</html>
```